Painting Valtoni Renovations New buildings

Paint jobs plasterwork renovations new building customer painter paper drywall Entsorgungen.neukunden win color splash pleasure in colors competent clean fast reliable new try build demolition color combinations color concepts offers washing façade painting wood stains new projects old building renovations yes no beautiful new old sell secure solve paint over paint paint spray paint lye assemble disassemble sell buy trade oil dust new old assembly disassembly putty sanding fashion devastation copying belief feng shui kleopatra pompes beer colors swamp lime abrasion release tighten

Target Market(s)

construction industry

Contact Information for Business Card

Maler

Font styles to use
Serif

Colors
f04a50
959595

Requirements
Must have
• elegant appearance
Nice to have
• simply goal-oriented clientele in detail
Should not have
• too colorful

```html
<!DOCTYPE html>
<html lang="de">
<head>
<meta charset="utf-8">
<title>Valtoni Malerbetrieb – Visitenkarte</title>
<link rel="stylesheet" href="https://fonts.googleapis.com/css2?family=Nunito+Sans:wght@400;800&display=swap">
<style>
  :root {
    --bg: #e4e4e4;
    --card: #f7f7f7;
    --brand-blue: #1d3f8c;
    --accent-red: #e23d4b;
    --text-dark: #1e1e1e;
    --shadow: rgba(0,0,0,0.18);
  }
  * { box-sizing: border-box; margin: 0; padding: 0; }
  html, body {
    width: 1200px; height: 1021px; overflow: hidden;
    background: var(--bg);
    font-family: "Nunito Sans", "Avenir", sans-serif;
  }
  .sheet {
    position: relative; width: 1200px; height: 1021px;
  }
  .card {
    position: absolute; left: 290px;
    width: 620px; height: 400px;
    background: var(--card);
    box-shadow: 0 6px 18px var(--shadow);
  }
  .card--front { top: 55px; }
  .card--back { top: 566px; }

  .wordmark {
    position: absolute; inset: 0;
    display: flex; align-items: center; justify-content: center; gap: 14px;
  }
  .wordmark__dot {
    width: 22px; height: 22px; border-radius: 50%;
    background: var(--brand-blue);
  }
  .wordmark__name {
    color: var(--brand-blue);
    font-weight: 800; font-size: 46px; letter-spacing: 0.5px;
  }

  .holder-name {
    position: absolute; left: 60px; top: 150px;
    color: var(--accent-red);
    font-weight: 800; font-size: 28px;
  }
  .brush-art {
    position: absolute; left: 220px; top: 196px;
    width: 170px; height: 80px;
  }
  .contact {
    position: absolute; left: 400px; top: 150px;
    color: var(--text-dark); font-size: 17px; line-height: 1.3;
    list-style: none;
  }
  .contact__address { margin-bottom: 6px; }
  .contact__line { display: flex; align-items: center; gap: 7px; }
  .contact__icon { width: 13px; height: 13px; flex: none; }
</style>
</head>
<body>
<main class="sheet">
  <section class="card card--front" aria-label="Vorderseite">
    <div class="wordmark">
      <span class="wordmark__dot"></span>
      <span class="wordmark__name">Valtoni Malerbetrieb</span>
    </div>
  </section>

  <section class="card card--back" aria-label="Rückseite">
    <h1 class="holder-name">Merenda Valtoni</h1>
    <svg class="brush-art" viewBox="0 0 170 80" role="img" aria-label="Pinsel mit farbigem Pinselstrich">
      <defs>
        <linearGradient id="stroke-tones" x1="0" y1="0" x2="1" y2="0">
          <stop offset="0" stop-color="#e84a5a"/>
          <stop offset="0.45" stop-color="#8cc8e8"/>
          <stop offset="1" stop-color="#2b4c94"/>
        </linearGradient>
      </defs>
      <rect x="0" y="0" width="170" height="80" rx="10" fill="url(#stroke-tones)"/>
    </svg>
    <ul class="contact">
      <li class="contact__address">Mühlegasse 17<br>8300 Kornfeld</li>
      <li class="contact__line">
        <svg class="contact__icon" viewBox="0 0 16 16"><path d="M4 1l3 3-2 2c1 2 3 4 5 5l2-2 3 3-2 3C7 15 1 9 1 3z" fill="var(--accent-red)"/></svg>
        +41 79 512 40 63
      </li>
      <li class="contact__line">
        <svg class="contact__icon" viewBox="0 0 16 16"><rect x="1" y="3" width="14" height="10" fill="none" stroke="var(--accent-red)" stroke-width="1.5"/><path d="M1 3l7 6 7-6" fill="none" stroke="var(--accent-red)" stroke-width="1.5"/></svg>
        merenda@valtoni-maler.ch
      </li>
      <li class="contact__line">
        <svg class="contact__icon" viewBox="0 0 16 16"><circle cx="8" cy="8" r="6.5" fill="none" stroke="var(--accent-red)" stroke-width="1.4"/><ellipse cx="8" cy="8" rx="3" ry="6.5" fill="none" stroke="var(--accent-red)" stroke-width="1.2"/><path d="M1.5 8h13" stroke="var(--accent-red)" stroke-width="1.2"/></svg>
        www.valtoni-maler.ch
      </li>
    </ul>
  </section>
</main>
</body>
</html>
```